Redesign Craft Brewing Recipe Website

Originally built with Bootstrap just to get the site going, I am seeking a complete redesign of the sites home page and recipe page. I am an experienced web developer with no graphic background, initially just looking for psd mocks.

I prefer styles that are clean and modern, and would prefer anything that is fun, engaging, and has an organic feel to it. I currently have a cartoon rabbit as a logo, but it needs some modification/tweaking, so any help in that area would be great as well.

Current site:
http://kettlefinch.hostgridapps.net/

Current launch page/logo:
http://www.kettlefinch.com/

I like the overall layout of the elements currently, but the design sucks.
Updates

The launch page is at the following URL

Reason: Still looking for a more modern design. Designs received so far are too similar to the original.

My site is content based and does not contain images or products. Your design should not consist of large images.

Reason: The website has very little images, so the designs need to be more text and content based. The header needs to be very small and should not contain an ad rotater.

Target Market(s)

Home brewers, Craft brewers, Microbreweries, Brewpubs

Requirements
Must have
• Web 2.0 Look and Feel, Fun, Hip, Focus on content
Should not have
• A large photo as a header

```html
<!DOCTYPE html>
<html lang="en">
<head>
<meta charset="utf-8">
<title>Kettlefinch – Craft Beer Recipes</title>
<link href="https://fonts.googleapis.com/css2?family=Barlow:wght@400;500;600&display=swap" rel="stylesheet">
<style>
  :root {
    --navy: #00577a;
    --sky-top: #00b4f0;
    --sky-bottom: #005578;
    --orange: #ff4f00;
    --white: #ffffff;
    --page: #ffffff;
    --text-blue: #00577a;
  }
  * { margin: 0; padding: 0; box-sizing: border-box; }
  html, body {
    width: 1200px; height: 1200px; overflow: hidden;
    background: var(--page);
    font-family: "Barlow", Arial, sans-serif;
  }
  .site {
    position: absolute; left: 46px; top: 197px;
    width: 1106px; height: 831px;
    display: flex; flex-direction: column;
    border-bottom: 2px solid var(--navy);
  }
  .topbar {
    height: 54px; background: var(--navy);
    position: relative; flex: none;
  }
  .topbar__brand {
    position: absolute; left: 158px; top: 11px;
    font-size: 30px; font-weight: 500; color: var(--white);
    letter-spacing: 0.5px; line-height: 32px;
  }
  .topbar__nav {
    position: absolute; left: 368px; top: 20px;
    display: flex; gap: 32px; list-style: none;
    font-size: 13px; line-height: 14px;
  }
  .topbar__nav a { color: var(--white); text-decoration: none; }
  .topbar__nav a.is-active { color: var(--orange); }
  .topbar__login {
    position: absolute; right: 158px; top: 17px;
    font-size: 17px; font-weight: 600; color: var(--white);
    text-decoration: none;
  }
  .main {
    flex: 1; position: relative;
    background: linear-gradient(to bottom, var(--sky-top) 0%, #0088c0 45%, var(--sky-bottom) 100%);
  }
  .hero {
    position: absolute; left: 157px; top: 25px;
    width: 792px; height: 152px; background: var(--navy);
    padding: 28px 31px;
    color: var(--white);
  }
  .hero__brand {
    font-size: 50px; font-weight: 500; line-height: 50px; letter-spacing: 0.5px;
  }
  .hero__tagline { font-size: 16px; margin-top: 6px; }
  .hero__like {
    display: flex; align-items: center; gap: 4px;
    margin-top: 10px; font-size: 9px;
  }
  .hero__like-box { width: 13px; height: 13px; background: var(--white); border-radius: 2px; }
  .sidebar {
    position: absolute; left: 157px; top: 209px;
    width: 196px; height: 488px; background: var(--navy);
    padding: 14px;
  }
  .search__field {
    display: block; width: 168px; height: 26px;
    background: var(--white); border: none;
  }
  .search__go {
    display: block; margin: 8px 0 0 136px;
    width: 32px; height: 32px; border: none;
    background: var(--orange); color: var(--white);
    font: 600 19px "Barlow", Arial, sans-serif;
  }
  .filters { list-style: none; margin-top: 16px; }
  .filters li {
    display: flex; align-items: center; gap: 7px;
    color: var(--white); font-size: 13px; height: 36px;
  }
  .filters__box { width: 10px; height: 10px; background: var(--white); }
  .feed { position: absolute; left: 371px; top: 209px; width: 578px; }
  .tabs { display: flex; gap: 9px; }
  .tabs__item {
    width: 101px; height: 36px; line-height: 36px;
    text-align: center; font-size: 13px; color: var(--white);
    background: var(--navy);
  }
  .tabs__item.is-active { background: var(--orange); }
  .recipe {
    height: 95px; background: var(--white);
    margin-top: 25px; padding: 22px 11px 0;
    color: var(--text-blue);
  }
  .recipe:first-of-type { margin-top: 15px; }
  .recipe__title { font-size: 17px; font-weight: 400; }
  .recipe__desc { font-size: 16px; margin-top: 6px; }
  .footer { height: 53px; background: var(--orange); flex: none; }
</style>
</head>
<body>
  <div class="site">
    <header class="topbar">
      <div class="topbar__brand">KETTLEFINCH</div>
      <ul class="topbar__nav">
        <li><a class="is-active" href="#">HOME</a></li>
        <li><a href="#">RECIPIES</a></li>
      </ul>
      <a class="topbar__login" href="#">LOGIN</a>
    </header>
    <main class="main">
      <section class="hero">
        <div class="hero__brand">KETTLEFINCH</div>
        <p class="hero__tagline">Kettlefinch is the easiest way to create and share craft beer recipies</p>
        <div class="hero__like"><span class="hero__like-box"></span>like</div>
      </section>
      <aside class="sidebar">
        <form class="search">
          <input class="search__field" type="text" aria-label="Search">
          <button class="search__go" type="button">Go</button>
        </form>
        <ul class="filters">
          <li>Brewing <span class="filters__box"></span></li>
          <li>Styles <span class="filters__box"></span></li>
          <li>Match Maker <span class="filters__box"></span></li>
        </ul>
      </aside>
      <section class="feed">
        <div class="tabs">
          <div class="tabs__item is-active">RECENT</div>
          <div class="tabs__item">POPULAR</div>
        </div>
        <article class="recipe">
          <h3 class="recipe__title">RECIPIE 1</h3>
          <p class="recipe__desc">Recipie Description etc.</p>
        </article>
        <article class="recipe">
          <h3 class="recipe__title">RECIPIE 2</h3>
          <p class="recipe__desc">Recipie Description etc.</p>
        </article>
        <article class="recipe">
          <h3 class="recipe__title">RECIPIE 3</h3>
          <p class="recipe__desc">Recipie Description etc.</p>
        </article>
      </section>
    </main>
    <footer class="footer"></footer>
  </div>
</body>
</html>
```